Flyer für eine mobile Reiseberatung
Zielgruppe
Ich habe eine mobile Reiseberatung, bin also ein Reisebüro nur ohne Geschäft und ohne Öffnungszeiten. Zielgruppe sind Menschen, die bei der Reiseplanung und Buchung Unterstützung möchten.
Aufgabenstellung
Ich möchte ein klares und schlichtes Design das aber auch Eyecatcher hat, die die Leute dazu bewegen den Flyer mitzunehmen. Die Leute sollen sofort erkennen, dass es um ein Reisebüro geht.
Für den Texr habe ich keine genauen Vorgaben. Kurz und prägnant, die Vorteile der mobilen Reiseberstung gegenüber stationären (zb keine festen Öffnungszeiten, immer erreichbar, flexibel usw) und gegenüber Plattformen im Internet ( zb persönlicher Ansprechpartner, schnelle Hilfe usw).
Ansonsten soll natürlich das Thema Reisen aufgegriffen werden und ein paar Infos zu mir (trage ich dann selber ein(
Außerdem Platzhalter für QR Codes Pixoramo / Kontaktvel
Und natürlich Kontaktdsten
Format: da ich die Flyer in Geschäften auslegen möchte wäre es ein doppelseitiger Flyer der nicht gefaltet wird, größe sollte Standard sein was Druckereien so haben

```html
<!DOCTYPE html>
<html lang="de">
<head>
<meta charset="utf-8">
<title>Feld Reisen – Flyer mobile Reiseberatung</title>
<link rel="stylesheet" href="https://fonts.googleapis.com/css2?family=Bebas+Neue&family=Figtree:wght@400;500;600&family=Outfit:wght@400;500;600;700&display=swap">
<style>
  :root{
    --stage:#b3b3b3;
    --navy:#1a2f5c;
    --brand-blue:#0e6fa3;
    --deep-blue:#11336a;
    --mid-blue:#0b6ca6;
    --sky:#7cb9e6;
    --pale:#eef7fc;
    --orange:#d6922c;
    --white:#ffffff;
    --ink:#111418;
  }
  *{box-sizing:border-box;margin:0;padding:0}
  html,body{width:1200px;height:1117px;overflow:hidden;background:var(--stage)}
  body{position:relative;font-family:"Figtree",Arial,sans-serif;color:var(--ink)}
  .flyer{position:absolute;top:193px;width:513px;height:725px;background:var(--white);overflow:hidden}
  .flyer--front{left:89px}
  .flyer--back{left:628px}
  .abs{position:absolute}
  svg.layer{position:absolute;left:0;top:0}

  /* front */
  .hero-photo{left:0;top:0;width:513px;height:350px;
    background:linear-gradient(100deg,#33bccd 0%,#6fd0dc 30%,#d9eef0 55%,#f3e6da 75%,#e8dccb 100%)}
  .hero-fade{left:0;top:200px;width:513px;height:160px;background:linear-gradient(180deg,rgba(255,255,255,0) 0%,rgba(255,255,255,.75) 70%,#fff 100%)}
  .palm-photo{left:330px;top:250px;width:190px;height:100px;border-radius:60% 0 0 40%;
    background:radial-gradient(ellipse at 60% 40%,#7c9a4a 0%,#a9b878 45%,rgba(240,230,215,0) 75%)}
  .brand{left:30px;top:40px;width:200px;text-align:center}
  .brand__dot{display:block;width:62px;height:62px;border-radius:50%;background:var(--orange);margin:0 auto 14px}
  .brand__name{font-family:"Outfit",Arial,sans-serif;font-weight:600;font-size:30px;color:var(--brand-blue);line-height:1}
  .headline{left:39px;top:232px;color:var(--navy)}
  .headline__pre{font-family:"Outfit",Arial,sans-serif;font-weight:500;font-size:36px;line-height:1;letter-spacing:.5px}
  .headline__main{font-family:"Bebas Neue",Impact,sans-serif;font-size:62px;line-height:.95;margin-top:2px}
  .section-title{font-family:"Outfit",Arial,sans-serif;font-weight:700;color:var(--brand-blue);text-transform:uppercase}
  .about{left:39px;top:517px;width:215px}
  .about .section-title{font-size:17px;margin-bottom:3px}
  .body-copy{font-size:10.9px;line-height:13.4px}
  .benefits{left:278px;top:504px;width:220px}
  .benefits .section-title{font-size:14.2px;line-height:16px}
  .benefits__rule{width:107px;height:2px;background:var(--sky);margin:8px 0 12px}
  .benefits ul{list-style:none}
  .benefits li{position:relative;padding-left:22px;font-family:"Outfit",Arial,sans-serif;font-weight:600;font-size:14.4px;line-height:16px;text-transform:uppercase;margin-bottom:11px}
  .benefits li svg{position:absolute;left:0;top:1px}

  /* back */
  .back-title{left:0;top:24px;width:513px;text-align:center;font-family:"Outfit",Arial,sans-serif;font-weight:700;font-size:22.5px;color:var(--white);letter-spacing:.3px}
  .service{left:48px;width:440px;height:74px}
  .service__photo{position:absolute;left:0;top:0;width:150px;height:72px;border:3px solid #fff;box-shadow:0 1px 4px rgba(0,0,0,.35)}
  .service__icon{position:absolute;left:133px;top:18px;width:38px;height:38px}
  .service__title{position:absolute;left:179px;top:0;font-family:"Outfit",Arial,sans-serif;font-weight:600;font-size:15.5px;color:var(--navy)}
  .service__text{position:absolute;left:180px;top:21px;width:245px;font-size:10.1px;line-height:12.4px}
  .photo-work{background:linear-gradient(135deg,#5b6470,#e9e8e6 55%,#bfc3c8)}
  .photo-temple{background:linear-gradient(180deg,#8fb2d3 0%,#e7c98f 40%,#5b7b3a 70%,#3d5e2a 100%)}
  .photo-case{background:linear-gradient(180deg,#3a3a3a 0%,#f2c21e 30%,#f0b418 80%,#222 100%)}
  .back-copy{left:44px;top:400px;width:210px;color:var(--white);font-size:10.9px;line-height:12.8px}
  .cta{left:44px;top:571px;width:425px;height:52px;border-radius:5px;background:var(--sky);color:var(--white);
    font-family:"Outfit",Arial,sans-serif;font-weight:600;font-size:14px;line-height:15px;text-align:center;display:flex;align-items:center;justify-content:center}
  .help{left:44px;top:640px;width:425px;display:flex;align-items:center;gap:14px}
  .help__rule{flex:1;height:2px;background:var(--orange)}
  .help__label{font-family:"Outfit",Arial,sans-serif;font-weight:600;font-size:18.5px;color:var(--orange)}
  .contact-bar{left:44px;top:664px;width:430px;display:flex;align-items:center;gap:12px;color:var(--white)}
  .phone{display:flex;align-items:center;gap:5px;font-family:"Outfit",Arial,sans-serif;font-weight:600;font-size:28px;line-height:1;white-space:nowrap}
  .contact{font-family:"Outfit",Arial,sans-serif;font-weight:500;font-size:10.6px;line-height:15px;white-space:nowrap}
  .contact div{display:flex;align-items:center;gap:4px}
</style>
</head>
<body>

<!-- front side -->
<section class="flyer flyer--front">
  <div class="abs hero-photo" role="img" aria-label="Luftaufnahme von türkisem Meer und hellem Sandstrand"></div>
  <div class="abs palm-photo" role="img" aria-label="Palmenkronen von oben"></div>
  <div class="abs hero-fade"></div>

  <svg class="layer" width="513" height="725" viewBox="0 0 513 725">
    <defs>
      <linearGradient id="boatGrad" x1="0" y1="0" x2="0" y2="1">
        <stop offset="0" stop-color="#6fa6d6"/><stop offset=".45" stop-color="#3f8d92"/><stop offset="1" stop-color="#8b6a4b"/>
      </linearGradient>
      <linearGradient id="forestGrad" x1="0" y1="0" x2="0" y2="1">
        <stop offset="0" stop-color="#2f5a26"/><stop offset=".6" stop-color="#6f9b4a"/><stop offset="1" stop-color="#4a6f3a"/>
      </linearGradient>
      <linearGradient id="poolGrad" x1="0" y1="0" x2="0" y2="1">
        <stop offset="0" stop-color="#a9dde0"/><stop offset="1" stop-color="#6ec1c9"/>
      </linearGradient>
      <linearGradient id="hikeGrad" x1="0" y1="0" x2="0" y2="1">
        <stop offset="0" stop-color="#8fb6d8"/><stop offset=".5" stop-color="#9fb0b8"/><stop offset="1" stop-color="#6d8a38"/>
      </linearGradient>
      <clipPath id="bandClip">
        <path d="M0,342 C140,322 330,322 513,350 L513,520 L0,520 Z"/>
      </clipPath>
    </defs>

    <circle cx="369" cy="121" r="145" fill="var(--sky)"/>
    <circle cx="369" cy="121" r="134" fill="#fff"/>
    <circle cx="369" cy="121" r="125" fill="url(#boatGrad)" role="img" aria-label="Frau mit Hut im Longtailboot vor Kalkfelsen"/>

    <g clip-path="url(#bandClip)">
      <rect x="0" y="320" width="171" height="200" fill="url(#forestGrad)" role="img" aria-label="Wasserfall im grünen Wald"/>
      <rect x="171" y="320" width="171" height="200" fill="url(#poolGrad)" role="img" aria-label="Person steigt in türkises Wasser"/>
      <rect x="342" y="320" width="171" height="200" fill="url(#hikeGrad)" role="img" aria-label="Wanderin auf einem Berggrat"/>
    </g>

    <path d="M0,507 C90,470 190,456 257,459 L257,725 L0,725 Z" fill="#fff"/>
    <path d="M257,459 C350,456 450,472 513,503 L513,725 L257,725 Z" fill="var(--pale)"/>
    <path d="M0,725 C110,684 240,672 350,690 C430,702 485,698 513,680 L513,725 Z" fill="var(--orange)"/>
    <path d="M0,705 C110,667 240,660 350,676 C430,688 485,686 513,668 L513,682 C485,700 430,704 350,692 C240,674 110,686 0,725 Z" fill="#fff"/>
  </svg>

  <div class="abs brand">
    <span class="brand__dot"></span>
    <div class="brand__name">Feld Reisen</div>
  </div>

  <h1 class="abs headline">
    <div class="headline__pre">BIST DU</div>
    <div class="headline__main">URLAUBSREIF?</div>
  </h1>

  <div class="abs about">
    <h2 class="section-title">Über uns</h2>
    <p class="body-copy">Lorem ipsum dolor sit amet, consectetur adipiscing elit, sed do eiusmod tempor incididunt ut labore et dolore magna aliqua. Ut enim adminim veniam, quis nostrud exercitation ullamco laboris nisi ut aliquip ex ea commodo consequat. Duis aute irure dolor in reprehenderit in voluptate velit esse cillum dolore eu fugiat nulla pariatur.</p>
  </div>

  <div class="abs benefits">
    <h2 class="section-title">Die Vorteile der<br>mobilen Reiseberstung<br>gegenüber stationären</h2>
    <div class="benefits__rule"></div>
    <ul>
      <li><svg width="15" height="13" viewBox="0 0 15 13"><path d="M1 7 L5.5 11 L14 1.5" fill="none" stroke="var(--orange)" stroke-width="3"/></svg>Keine festen<br>Öffnungszeiten,</li>
      <li><svg width="15" height="13" viewBox="0 0 15 13"><path d="M1 7 L5.5 11 L14 1.5" fill="none" stroke="var(--orange)" stroke-width="3"/></svg>Immer erreichbar</li>
      <li><svg width="15" height="13" viewBox="0 0 15 13"><path d="M1 7 L5.5 11 L14 1.5" fill="none" stroke="var(--orange)" stroke-width="3"/></svg>Flexibel</li>
    </ul>
  </div>
</section>

<!-- back side -->
<section class="flyer flyer--back">
  <svg class="layer" width="513" height="725" viewBox="0 0 513 725">
    <defs>
      <linearGradient id="backBlue" x1="0" y1="0" x2="0" y2="1">
        <stop offset="0" stop-color="var(--mid-blue)"/><stop offset="1" stop-color="var(--deep-blue)"/>
      </linearGradient>
      <linearGradient id="hikerGrad" x1="0" y1="0" x2="0" y2="1">
        <stop offset="0" stop-color="#d6e7f3"/><stop offset=".45" stop-color="#9db8cc"/><stop offset=".7" stop-color="#8b9a4a"/><stop offset="1" stop-color="#6a7a34"/>
      </linearGradient>
      <clipPath id="circleCut"><rect x="0" y="0" width="513" height="571"/></clipPath>
    </defs>
    <path d="M0,0 H513 V88 C440,64 330,52 230,58 C140,63 60,76 0,72 Z" fill="var(--orange)"/>
    <path d="M0,377 C110,350 250,340 330,345 C420,350 480,362 513,372 V725 H0 Z" fill="#a9d0f0"/>
    <path d="M0,393 C110,362 250,352 330,356 C420,361 480,376 513,390 V725 H0 Z" fill="url(#backBlue)"/>
    <g clip-path="url(#circleCut)">
      <circle cx="372" cy="493" r="116" fill="#fff"/>
      <circle cx="372" cy="493" r="108" fill="url(#hikerGrad)" role="img" aria-label="Wanderin mit rotem Rucksack auf einem Bergpfad"/>
    </g>
  </svg>

  <h2 class="abs back-title">UNSERE PERSÖNLICHEN LEISTUNGEN</h2>

  <article class="abs service" style="top:95px">
    <div class="service__photo photo-work" role="img" aria-label="Hände am Schreibtisch mit Kaffeetasse und Notizen"></div>
    <svg class="service__icon" viewBox="0 0 38 38"><circle cx="19" cy="19" r="18" fill="var(--mid-blue)" stroke="#fff" stroke-width="2"/><rect x="10" y="11" width="14" height="10" rx="2" fill="none" stroke="#fff" stroke-width="1.6"/><path d="M13 21 L12 25 L16 21" fill="#fff"/><rect x="17" y="18" width="12" height="9" rx="2" fill="#fff"/></svg>
    <h3 class="service__title">Persönliche Beratung</h3>
    <p class="service__text">Vor Ort, telefonisch oder per E-Mail. Melden Sie sich und wir finden die passende Reise für Sie. Wohin Sie auch reisen, wir schonen Ihre Reisekasse</p>
  </article>

  <article class="abs service" style="top:179px">
    <div class="service__photo photo-temple" role="img" aria-label="Tempel am See vor Bergen"></div>
    <svg class="service__icon" viewBox="0 0 38 38"><circle cx="19" cy="19" r="18" fill="var(--mid-blue)" stroke="#fff" stroke-width="2"/><circle cx="19" cy="19" r="9" fill="none" stroke="#fff" stroke-width="1.6"/><ellipse cx="19" cy="19" rx="4" ry="9" fill="none" stroke="#fff" stroke-width="1.4"/><line x1="10" y1="19" x2="28" y2="19" stroke="#fff" stroke-width="1.4"/></svg>
    <h3 class="service__title">Reisen aller Art</h3>
    <p class="service__text">individuelle Reisevorstellungen, zusätzliche Reiseleistungen wie Mietwagen, Transfers oder Parken am Flughafen... Wir organisieren es gerne für Sie.</p>
  </article>

  <article class="abs service" style="top:263px">
    <div class="service__photo photo-case" role="img" aria-label="Geöffneter gelber Koffer mit Reiseutensilien"></div>
    <svg class="service__icon" viewBox="0 0 38 38"><circle cx="19" cy="19" r="18" fill="var(--mid-blue)" stroke="#fff" stroke-width="2"/><path d="M19 9 L27 12 V19 C27 24 23 27.5 19 29 C15 27.5 11 24 11 19 V12 Z" fill="none" stroke="#fff" stroke-width="2"/><path d="M19 12 L24 14 V19 C24 22 22 24.5 19 25.8 Z" fill="#fff"/></svg>
    <h3 class="service__title">Schutz vor und auf der Reise</h3>
    <p class="service__text">Mit der Novaro Travel Card sind Sie rundum versorgt. Wir bieten Ihnen mit diesem Komplettpaket ein optimales Produkt.</p>
  </article>

  <p class="abs back-copy">Lorem ipsum dolor sit amet, consectetur adipiscing elit, sed do eiusmod tempor incididunt ut labore et dolore magna aliqua. Ut enim adminim veniam, quis nostrud exercitation ullamco laboris nisi ut aliquip ex ea commodo consequat. Duis aute irure dolor in reprehenderit in voluptate velit esse cillum dolore eu fugiat nulla pariatur. Excepteur sint occaecat cupidatat non proident, sunt in culpa qui officia deserunt mollit anim id est laborum.</p>

  <div class="abs cta">Entdecken Sie die besten Reiseangebote mit unserem<br>kostenlosen Home Travel Service!</div>

  <div class="abs help"><span class="help__rule"></span><span class="help__label">schnelle Hilfe</span><span class="help__rule"></span></div>

  <div class="abs contact-bar">
    <div class="phone">
      <svg width="14" height="24" viewBox="0 0 16 26"><path d="M6 1 C2 3 1 8 1 13 C1 18 2 23 6 25 L9 20 C7 18 6 16 6 13 C6 10 7 8 9 6 Z" fill="#fff"/></svg>
      01609382716
    </div>
    <div class="contact">
      <div><svg width="10" height="10" viewBox="0 0 10 10"><circle cx="5" cy="5" r="4.3" fill="none" stroke="#fff" stroke-width="1"/><rect x="2.6" y="3.3" width="4.8" height="3.4" fill="none" stroke="#fff" stroke-width=".8"/></svg>tamara.feld@reisetarifblick.de</div>
      <div><svg width="10" height="10" viewBox="0 0 10 10"><circle cx="5" cy="5" r="4.3" fill="none" stroke="#fff" stroke-width="1"/><ellipse cx="5" cy="5" rx="1.8" ry="4.3" fill="none" stroke="#fff" stroke-width=".8"/><line x1=".7" y1="5" x2="9.3" y2="5" stroke="#fff" stroke-width=".8"/></svg>tamarofeld.reisetarifblick.de</div>
    </div>
  </div>
</section>

</body>
</html>
```